Electrical Contracting business card design

We need a simple business card design for an Electrical Contracting business. A simple design would be appreciated
This company has 2 directors so on one it would have Colin Marsh & another with Dana Marsh.
Updates

Reason: Hello A few designers have asked for a logo unfortunately we don't have one so have extended deadline to see who can help us out with this. CHEERS

Reason: Waiting for business partner to return from xmas break. cheers

Industry/Entity Type

Business

Contact Information for Business Card

Volmera Electrical Services P/L
REC: 36074
Residential Commercial Industrial
Service-Repairs-Renovations-Installations-Telephone-Data
Colin Marsh-Ph: 0433 517 862
Email: colin@volmeraelectrical.com.au

Requirements
Should not have
• The design should not have any electrical appliances in it ie: power-points, leads, houses etc.

```html
<!DOCTYPE html>
<html lang="en">
<head>
<meta charset="utf-8">
<title>Volmera Electrical Services – Business Card</title>
<link href="https://fonts.googleapis.com/css2?family=Open+Sans:wght@300;400;600&display=swap" rel="stylesheet">
<style>
  :root {
    --page-bg: #ece9e4;
    --card-bg: #ffffff;
    --ink: #111418;
    --brand-blue: #1a7fbf;
    --band-top: #0aa0d6;
    --band-bottom: #0a6a9e;
    --bullet: #7fd3f2;
    --card-shadow: 0 10px 30px rgba(0,0,0,0.18);
  }
  * { box-sizing: border-box; margin: 0; padding: 0; }
  html, body {
    width: 1200px; height: 1000px; overflow: hidden;
    background: var(--page-bg);
    font-family: "Open Sans", Arial, sans-serif;
    color: var(--ink);
  }
  .canvas { position: relative; width: 1200px; height: 1000px; }

  .card {
    position: absolute;
    width: 700px; height: 420px;
    background: var(--card-bg);
    box-shadow: var(--card-shadow);
    overflow: hidden;
  }
  .card--front { left: 60px; top: 60px; }
  .card--back { left: 440px; top: 520px; }

  /* Wordmark */
  .wordmark { display: flex; align-items: center; }
  .wordmark__square { background: var(--brand-blue); flex: none; }
  .wordmark__name {
    font-weight: 600; color: var(--ink); line-height: 1.1;
  }

  .card--front .wordmark {
    position: absolute; left: 50%; top: 50%;
    transform: translate(-50%, -50%);
    flex-direction: column; gap: 22px;
  }
  .card--front .wordmark__square { width: 200px; height: 200px; }
  .card--front .wordmark__name { font-size: 34px; text-align: center; }

  .card--back .brand-block {
    position: absolute; left: 70px; top: 40px;
    display: flex; flex-direction: column; align-items: center; gap: 10px;
    width: 150px;
  }
  .card--back .wordmark { flex-direction: column; gap: 10px; }
  .card--back .wordmark__square { width: 110px; height: 110px; }
  .card--back .wordmark__name { font-size: 16px; text-align: center; }
  .licence { font-size: 14px; font-weight: 600; color: var(--ink); }

  .contact {
    position: absolute; right: 45px; top: 40px; text-align: right;
  }
  .contact__name { font-weight: 300; font-size: 48px; line-height: 1.1; }
  .contact__line { font-weight: 300; font-size: 22px; color: var(--brand-blue); line-height: 1.35; }

  .services-band {
    position: absolute; left: 0; right: 0; bottom: 0; height: 150px;
    background: linear-gradient(to bottom, var(--band-top), var(--band-bottom));
    display: flex; justify-content: space-around; align-items: center;
    padding: 0 40px;
  }
  .services-list { list-style: none; }
  .services-list li {
    color: #ffffff; font-size: 22px; line-height: 1.35;
    display: flex; align-items: center; gap: 10px;
  }
  .services-list li::before {
    content: ""; width: 6px; height: 6px; border-radius: 50%;
    background: var(--bullet);
  }
  .services-list--low { margin-top: 30px; }
  .services-list--high { margin-top: -30px; }
</style>
</head>
<body>
<main class="canvas">
  <section class="card card--front" aria-label="Card front">
    <div class="wordmark">
      <div class="wordmark__square"></div>
      <div class="wordmark__name">Volmera Electrical Services</div>
    </div>
  </section>

  <section class="card card--back" aria-label="Card back">
    <div class="brand-block">
      <div class="wordmark">
        <div class="wordmark__square"></div>
        <div class="wordmark__name">Volmera Electrical Services</div>
      </div>
      <div class="licence">P/L REC: 36074</div>
    </div>

    <div class="contact">
      <div class="contact__name">Colin Marsh</div>
      <div class="contact__line">Ph: 0433 517 862</div>
      <div class="contact__line">email: colin@volmeraelectrical.com.au</div>
    </div>

    <div class="services-band">
      <ul class="services-list services-list--low">
        <li>Residential</li><li>Commercial</li><li>Industrial</li>
      </ul>
      <ul class="services-list">
        <li>Service</li><li>Repairs</li><li>Renovations</li>
      </ul>
      <ul class="services-list services-list--high">
        <li>Installations</li><li>Telephone</li><li>Data</li>
      </ul>
    </div>
  </section>
</main>
</body>
</html>
```